Business card design for crowd sourced review site.

I need a business card magnet design for an online, crowd-sourced, restaurant review site strictly for Kosher restaurants.
It is similar to RoamLedger but catering to a very particular crowd.
The markets it will be distributed in are flooded with business card fridge magnets so this needs to be eye-catching and unique. The Business name is PlateMarks
The website isnt finished but you can see the basic setup here
http://restaurant.vintrello.com/

The second image i included is another logo design I liked and was thinking about using and decided I will probably also make a SECOND custom cut business card in the shape of that icon. Bonus if you can throw that in also.

Target Market(s)

Jewish consumers aged 20-35

Industry/Entity Type

Business

Contact Information for Business Card

see description.
Design should not be too crowded and should in eye-catching. Will mainly be used as fridge magnets.

Requirements
Must have
• Website address. logo.
Nice to have
• tagline. (The Definitive guide to kosher dining for the Kosher consumer)
• Im not a professional but I personally think the color blue goes along with this concept. ill leave it to you to decide.
Should not have
• any religious symbols.

```html
<!DOCTYPE html>
<html lang="en">
<head>
<meta charset="utf-8">
<title>PlateMarks Business Card</title>
<link rel="stylesheet" href="https://fonts.googleapis.com/css2?family=Open+Sans:wght@400;600;700&display=swap">
<style>
  :root {
    --page-bg: #9a9a9a;
    --card-black: #0d0d0d;
    --card-charcoal: #1e1e1e;
    --rule-white: #f2f2f2;
    --accent-red: #d8322a;
    --accent-orange: #ee7a45;
    --text-light: #f4f4f4;
    --herb-green: #3f7d2a;
  }
  html, body {
    margin: 0;
    width: 1200px;
    height: 1200px;
    overflow: hidden;
    background: var(--page-bg);
    font-family: "Open Sans", Arial, sans-serif;
  }
  .business-card {
    position: absolute;
    left: 75px;
    top: 300px;
    width: 1050px;
    height: 600px;
    overflow: hidden;
    border-radius: 4px;
    background: radial-gradient(ellipse at 30% 30%, var(--card-charcoal), var(--card-black) 70%);
    box-shadow: 0 10px 30px rgba(0,0,0,.35);
  }
  .herb-edge {
    position: absolute;
    left: 0; top: 0;
    width: 34px; height: 100%;
    background: linear-gradient(180deg, var(--herb-green), #6aa24a 40%, var(--accent-red) 75%, var(--herb-green));
  }
  .brand {
    position: absolute;
    left: 80px;
    top: 95px;
    display: flex;
    align-items: center;
    gap: 16px;
  }
  .brand-dot {
    width: 22px; height: 22px;
    border-radius: 50%;
    background: var(--accent-red);
  }
  .brand-name {
    font-size: 58px;
    font-weight: 600;
    color: var(--text-light);
    letter-spacing: 1px;
  }
  .contact {
    position: absolute;
    right: 70px;
    top: 40px;
    color: var(--text-light);
    font-size: 30px;
    line-height: 1.3;
  }
  .contact-name { font-weight: 700; font-size: 32px; }
  .contact-line { display: flex; align-items: center; gap: 12px; }
  .contact-line svg { width: 22px; height: 22px; }
  .strip-rule {
    position: absolute;
    left: 34px; right: 0;
    height: 4px;
    background: var(--rule-white);
  }
  .rule-top-outer { top: 206px; }
  .rule-top-inner { top: 218px; }
  .rule-bottom-inner { top: 478px; }
  .rule-bottom-outer { top: 490px; }
  .food-strip {
    position: absolute;
    left: 150px; right: 40px;
    top: 228px;
    height: 244px;
    display: flex;
    gap: 6px;
    background: var(--rule-white);
  }
  .food-photo { flex: 1; }
  .photo-wraps { background: linear-gradient(135deg, #8c1a14, #c8a56a 60%, #6d9a3a); }
  .photo-salad { background: linear-gradient(135deg, #d9d2b8, #c9332a 45%, #9cc35a); }
  .photo-steak { background: linear-gradient(135deg, #e8dcc0, #5a2f1e 55%, #8fb65a); }
  .photo-peppers { background: linear-gradient(135deg, #d8462a, #b8843a 55%, #e9e4dc); }
  .website {
    position: absolute;
    right: 60px;
    top: 515px;
    font-size: 44px;
    font-weight: 600;
    color: var(--accent-orange);
    letter-spacing: 1px;
  }
</style>
</head>
<body>
  <div class="business-card">
    <div class="herb-edge" role="img" aria-label="Fresh herbs and tomato border"></div>

    <div class="brand">
      <span class="brand-dot"></span>
      <span class="brand-name">PlateMarks</span>
    </div>

    <div class="contact">
      <div class="contact-name">Miriam</div>
      <div class="contact-line">
        <svg viewBox="0 0 22 22" aria-hidden="true"><rect width="22" height="22" fill="var(--accent-red)"/><path d="M6 5l3 0 1 4-2 1a8 8 0 0 0 4 4l1-2 4 1 0 3c-6 1-12-5-11-11z" fill="#fff"/></svg>
        <span>0417 582 903</span>
      </div>
      <div class="contact-line">
        <svg viewBox="0 0 22 22" aria-hidden="true"><rect width="22" height="22" fill="var(--accent-red)"/><rect x="7" y="4" width="8" height="14" rx="1.5" fill="#fff"/><rect x="8.5" y="6" width="5" height="8" fill="var(--accent-red)"/></svg>
        <span>7064129387</span>
      </div>
    </div>

    <div class="strip-rule rule-top-outer"></div>
    <div class="strip-rule rule-top-inner"></div>
    <div class="food-strip">
      <div class="food-photo photo-wraps" role="img" aria-label="Photo of stuffed wraps with tomato"></div>
      <div class="food-photo photo-salad" role="img" aria-label="Photo of fresh salad plate"></div>
      <div class="food-photo photo-steak" role="img" aria-label="Photo of grilled steak in flatbread"></div>
      <div class="food-photo photo-peppers" role="img" aria-label="Photo of roasted peppers and mushrooms"></div>
    </div>
    <div class="strip-rule rule-bottom-inner"></div>
    <div class="strip-rule rule-bottom-outer"></div>

    <div class="website">www.restaurant.vintrello.com</div>
  </div>
</body>
</html>
```